Online Travel Agency card design with 2 logos

Need a two sided business card design for online tourism agency which is based in Istanbul Turkey.
Need a business card design where it shows the travel agency logo but also the logo and information of the parent company as well.Parent company logo is just text with 2 different colors. (Arial font with text ToreVextra "Tore"- hex #172841 and "Vextra" hex-#FF7F00)
Both logos are uploaded.
Target Market(s)
travel , online
Industry/Entity Type
Travel
Contact Information for Business Card
The information on the card should be as :
Travel Agency Logo logo (pnlogo)
Parent Company logo(torelogo)
Company information :ToreVextra Turizm ve Bilgi Teknolojileri A.Ş
Address of company
Tel
Email
Name
Position(english and turkish)

```html
<!DOCTYPE html>
<html lang="tr">
<head>
<meta charset="utf-8">
<title>ToreVextra Business Card</title>
<link rel="stylesheet" href="https://fonts.googleapis.com/css2?family=Arimo:wght@400;700&display=swap">
<style>
  :root {
    --page-bg: #2b2b2d;
    --navy: #172841;
    --orange: #ff7f00;
    --white: #ffffff;
    --deep-blue: #1f3f8f;
    --violet: #3a2f8c;
    --ink: #1c2233;
  }
  * { box-sizing: border-box; margin: 0; padding: 0; }
  html, body { width: 1200px; height: 900px; overflow: hidden; }
  body {
    background: var(--page-bg);
    font-family: "Arimo", Arial, sans-serif;
    position: relative;
  }
  .card {
    position: absolute;
    left: 250px;
    width: 700px;
    height: 400px;
    overflow: hidden;
    border-radius: 4px;
    box-shadow: 0 10px 30px rgba(0,0,0,0.45);
  }
  .card--back { top: 35px; }
  .card--front { top: 465px; background: var(--white); }

  .card__art { position: absolute; inset: 0; }
  .card--back .card__art {
    background:
      radial-gradient(ellipse at 30% 20%, rgba(60,160,220,0.9), transparent 55%),
      radial-gradient(ellipse at 20% 75%, rgba(240,205,200,0.7), transparent 40%),
      radial-gradient(ellipse at 80% 15%, rgba(40,90,170,0.9), transparent 45%),
      linear-gradient(160deg, #2a7fc0 0%, var(--deep-blue) 45%, var(--violet) 100%);
  }
  .card--front .card__art {
    background:
      radial-gradient(ellipse at 85% 40%, rgba(233,181,106,0.85), transparent 35%),
      radial-gradient(ellipse at 40% 85%, rgba(31,180,227,0.95), transparent 55%),
      radial-gradient(ellipse at 60% 40%, rgba(80,190,220,0.6), transparent 45%),
      linear-gradient(180deg, #f7fbfd 0%, #e3f3fa 40%, #6cc8ea 100%);
  }

  .wordmark {
    display: flex; align-items: center; gap: 10px;
    font-weight: 700; letter-spacing: 0.5px; line-height: 1;
  }
  .wordmark__mark { flex: none; background: var(--orange); }

  .seal {
    position: absolute;
    left: 50%; top: 50%;
    width: 300px; height: 300px;
    margin: -150px 0 0 -150px;
    border-radius: 50%;
    background: rgba(30,45,110,0.55);
    border: 1.5px solid rgba(200,225,245,0.8);
    display: flex; flex-direction: column; align-items: center; justify-content: center;
    gap: 24px;
  }
  .seal .wordmark { color: var(--white); font-size: 42px; }
  .seal .wordmark__mark { width: 12px; height: 12px; }

  .agency {
    display: flex; align-items: center; gap: 6px;
    font-weight: 700; font-size: 22px; color: var(--white);
  }
  .agency__dot {
    width: 22px; height: 22px; border-radius: 50%;
    background: var(--navy);
  }

  .brand-block { position: absolute; left: 40px; top: 150px; }
  .brand-block .wordmark { color: var(--navy); font-size: 50px; }
  .brand-block .wordmark__mark { width: 14px; height: 14px; }
  .brand-block__legal {
    margin-top: 8px; font-size: 12px; font-weight: 700; color: var(--ink);
  }

  .frame {
    position: absolute; left: 330px; top: 40px;
    width: 340px; height: 300px;
  }

  .contact {
    position: absolute; left: 420px; top: 98px;
    color: var(--white);
  }
  .contact__name {
    display: flex; align-items: center; gap: 10px;
    font-size: 24px; font-weight: 700; letter-spacing: 1px;
  }
  .contact__role {
    margin: 5px 0 12px 36px; font-size: 12px; font-weight: 700; line-height: 1.35;
  }
  .contact__row {
    display: flex; align-items: center; gap: 12px;
    font-size: 12px; margin: 0 0 8px 6px;
  }
  .icon { width: 16px; height: 16px; flex: none; }
  .icon--lg { width: 26px; height: 26px; }

  .card--front .agency { position: absolute; left: 40px; bottom: 36px; }
</style>
</head>
<body>

<section class="card card--back">
  <div class="card__art" role="img" aria-label="Blue and violet watercolour wash background"></div>
  <div class="seal">
    <span class="wordmark"><span class="wordmark__mark"></span>ToreVextra</span>
    <span class="agency"><span class="agency__dot"></span>pratikrota</span>
  </div>
</section>

<section class="card card--front">
  <div class="card__art" role="img" aria-label="Light sky-blue and sand watercolour splash background"></div>

  <svg class="frame" viewBox="0 0 340 300" aria-hidden="true">
    <polyline points="0,30 230,0 340,0 340,230 110,300 0,300" fill="none" stroke="#1c2233" stroke-width="1"/>
  </svg>

  <div class="brand-block">
    <div class="wordmark"><span class="wordmark__mark"></span>ToreVextra</div>
    <div class="brand-block__legal">ToreVextra Turizm ve Bilgi Teknolojileri A.Ş</div>
  </div>

  <div class="contact">
    <div class="contact__name">
      <svg class="icon icon--lg" viewBox="0 0 26 26" aria-hidden="true">
        <circle cx="13" cy="13" r="13" fill="#1c2233"/>
        <circle cx="13" cy="10" r="4" fill="#fff"/>
        <path d="M6 20 q7 -8 14 0 z" fill="#fff"/>
      </svg>
      YOUR NAME
    </div>
    <div class="contact__role">Sales Manager / Satış Müdürü</div>
    <div class="contact__row">
      <svg class="icon" viewBox="0 0 16 16" aria-hidden="true"><circle cx="8" cy="8" r="8" fill="#1c2233"/><path d="M8 3.5a2.8 2.8 0 0 0-2.8 2.8C5.2 9 8 12.5 8 12.5s2.8-3.5 2.8-6.2A2.8 2.8 0 0 0 8 3.5z" fill="#fff"/></svg>
      Kadıköy, İstanbul, Türkiye
    </div>
    <div class="contact__row">
      <svg class="icon" viewBox="0 0 16 16" aria-hidden="true"><circle cx="8" cy="8" r="8" fill="#1c2233"/><rect x="5.5" y="3.5" width="5" height="9" rx="1" fill="#fff"/></svg>
      123-123-1234
    </div>
    <div class="contact__row">
      <svg class="icon" viewBox="0 0 16 16" aria-hidden="true"><circle cx="8" cy="8" r="8" fill="#1c2233"/><rect x="4" y="5" width="8" height="6" fill="#fff"/><polyline points="4,5 8,8.5 12,5" fill="none" stroke="#1c2233" stroke-width="0.8"/></svg>
      info@torevextra.com
    </div>
  </div>

  <span class="agency"><span class="agency__dot"></span>pratikrota</span>
</section>

</body>
</html>
```